Web Button design and production

I need remote control like buttons (or your own design of buttons if I like it)
3x4 text buttons (normal, pressed, disabled)
3x1 empty button (normal, pressed, disabled)
3x6 buttons with glyph (normal, pressed, disabled)
3x288 with 24h time "00:00", "00:05", "00:10" (normal, pressed, disabled)
4 LED (red, green, orange, black)
I will upload the background image as soon as possible (black plastic)
See attached images
Q: Do the buttons have to be gray/black?
A: It should look like a high end remote control. It could be brushed aluminum as well, or something you come up with. But I guess black or dark grey would be best. The background will be picsharbor 40561739, but it's not available yet.
Q: Do I have to provide all buttons for the contest?
A: No! I only need one button (3 states) and a LED to decide. Only the winner will do the whole job.
Q: Is the Designer who wins the contest expected to complete all the extra buttons?
A: Yes, please.
Plastic

```html
<!DOCTYPE html>
<html lang="en">
<head>
<meta charset="utf-8">
<title>Remote Control Buttons – Normal, Pressed, Disabled</title>
<link rel="stylesheet" href="https://fonts.googleapis.com/css2?family=Jost:wght@400;500&display=swap">
<style>
  :root {
    --bg: #1b1b1c;
    --bg-dark: #141415;
    --btn-top: #3a3a3c;
    --btn-mid: #161617;
    --btn-bottom: #050505;
    --btn-edge: #5a5a5c;
    --btn-shadow: rgba(0,0,0,0.85);
    --label: #f2f2f2;
    --label-pressed: #2f86e0;
    --pressed-top: #242426;
    --pressed-bottom: #0a0a0b;
    --disabled-top: #2b2b2c;
    --disabled-bottom: #1c1c1d;
    --label-disabled: #3c3c3e;
    --led-off: #6a6a6a;
    --led-green: #35c82b;
    --led-orange: #f5ae12;
    --led-red: #e0231b;
  }
  * { box-sizing: border-box; margin: 0; padding: 0; }
  html, body { width: 1108px; height: 1200px; overflow: hidden; }
  body {
    background:
      repeating-linear-gradient(45deg, rgba(255,255,255,0.018) 0 2px, transparent 2px 5px),
      repeating-linear-gradient(-45deg, rgba(0,0,0,0.25) 0 2px, transparent 2px 5px),
      radial-gradient(ellipse at 40% 30%, #222224, var(--bg-dark));
    font-family: "Jost", "Futura", sans-serif;
    position: relative;
  }
  .state-set { position: absolute; left: 0; width: 1108px; height: 400px; }
  .state-normal { top: 0; }
  .state-pressed { top: 405px; }
  .state-disabled { top: 804px; }

  .btn {
    position: absolute;
    display: flex; align-items: center; justify-content: center;
    border-radius: 12px;
    background: linear-gradient(180deg, var(--btn-top) 0%, var(--btn-mid) 48%, var(--btn-bottom) 52%, #111112 100%);
    border: 2px solid #0a0a0a;
    box-shadow: inset 0 2px 0 var(--btn-edge), inset 0 -2px 3px rgba(255,255,255,0.06), 0 5px 8px var(--btn-shadow);
    color: var(--label);
    text-align: center;
    text-transform: uppercase;
  }
  .state-pressed .btn {
    background: linear-gradient(180deg, var(--pressed-top) 0%, #121213 50%, var(--pressed-bottom) 100%);
    box-shadow: inset 0 3px 6px rgba(0,0,0,0.9), inset 0 -1px 0 rgba(255,255,255,0.08), 0 2px 4px var(--btn-shadow);
    color: var(--label-pressed);
  }
  .state-disabled .btn {
    background: linear-gradient(180deg, var(--disabled-top), var(--disabled-bottom));
    border-color: #161617;
    box-shadow: inset 0 1px 0 #3a3a3b, 0 3px 5px rgba(0,0,0,0.6);
    color: var(--label-disabled);
  }

  .btn-arrow { width: 117px; height: 100px; }
  .btn-text { width: 179px; height: 112px; font-size: 27px; line-height: 1.15; font-weight: 400; letter-spacing: 0.5px; }
  .btn-small { width: 120px; height: 66px; font-size: 26px; letter-spacing: 0.5px; }
  .btn-empty { width: 123px; height: 62px; }

  .btn svg { fill: currentColor; }
  .btn-arrow svg { width: 24px; height: 30px; }
  .btn-small svg { width: 44px; height: 36px; }

  .row-a-arrow { top: 45px; } .row-a-text { top: 34px; }
  .row-b-arrow { top: 212px; } .row-b-text { top: 206px; }
  .col-1 { left: 61px; } .col-2 { left: 204px; }
  .grid-c1 { left: 432px; } .grid-c2 { left: 583px; } .grid-c3 { left: 734px; }
  .grid-r1 { top: 34px; } .grid-r2 { top: 151px; } .grid-r3 { top: 260px; }

  .led {
    position: absolute; left: 881px; width: 46px; height: 46px; border-radius: 50%;
    border: 4px solid #2a2a2b;
    box-shadow: 0 0 0 2px #0c0c0c, 0 3px 6px rgba(0,0,0,0.8), inset 0 -4px 6px rgba(0,0,0,0.45);
  }
  .led::after {
    content: ""; position: absolute; left: 8px; top: 4px; width: 20px; height: 12px; border-radius: 50%;
    background: rgba(255,255,255,0.55); filter: blur(2px);
  }
  .led-off { top: 33px; background: radial-gradient(circle at 50% 60%, #8a8a8a, var(--led-off) 55%, #333 100%); }
  .led-green { top: 112px; background: radial-gradient(circle at 50% 60%, #9df58d, var(--led-green) 55%, #136a10 100%); }
  .led-orange { top: 193px; background: radial-gradient(circle at 50% 60%, #ffe08a, var(--led-orange) 55%, #8a5a05 100%); }
  .led-red { top: 271px; background: radial-gradient(circle at 50% 60%, #ff8a7e, var(--led-red) 55%, #6e0b07 100%); }
  .btn-empty.normal { left: 965px; top: 148px; }
</style>
</head>
<body>

<svg width="0" height="0" style="position:absolute" aria-hidden="true">
  <defs>
    <symbol id="icon-play" viewBox="0 0 24 30"><path d="M4 3 L21 15 L4 27 Z"/></symbol>
    <symbol id="icon-back" viewBox="0 0 24 30"><path d="M20 3 L3 15 L20 27 Z"/></symbol>
    <symbol id="icon-first" viewBox="0 0 44 36"><rect x="8" y="4" width="6" height="28"/><path d="M36 4 L16 18 L36 32 Z"/></symbol>
    <symbol id="icon-last" viewBox="0 0 44 36"><path d="M8 4 L28 18 L8 32 Z"/><rect x="30" y="4" width="6" height="28"/></symbol>
    <symbol id="icon-arrow-left" viewBox="0 0 44 36"><path d="M4 18 L18 6 L18 13 L40 13 L40 23 L18 23 L18 30 Z"/></symbol>
    <symbol id="icon-return" viewBox="0 0 44 36"><path d="M4 24 L16 13 L16 19 L28 19 C32 19 34 17 34 13 L34 6 L41 6 L41 14 C41 22 36 27 28 27 L16 27 L16 33 Z"/></symbol>
  </defs>
</svg>

<section class="state-set state-normal" aria-label="Normal state">
  <div class="btn btn-arrow col-1 row-a-arrow"><svg><use href="#icon-play"/></svg></div>
  <div class="btn btn-text col-2 row-a-text">Book<br>Now</div>
  <div class="btn btn-arrow col-1 row-b-arrow"><svg><use href="#icon-back"/></svg></div>
  <div class="btn btn-text col-2 row-b-text">Jetzt<br>Buchen</div>

  <div class="btn btn-small grid-c1 grid-r1"><svg><use href="#icon-first"/></svg></div>
  <div class="btn btn-small grid-c2 grid-r1"><svg><use href="#icon-last"/></svg></div>
  <div class="btn btn-small grid-c3 grid-r1"><svg><use href="#icon-arrow-left"/></svg></div>
  <div class="btn btn-small grid-c1 grid-r2">00:05</div>
  <div class="btn btn-small grid-c2 grid-r2">00:10</div>
  <div class="btn btn-small grid-c3 grid-r2"><svg><use href="#icon-return"/></svg></div>
  <div class="btn btn-small grid-c1 grid-r3">00:15</div>
  <div class="btn btn-small grid-c2 grid-r3">00:20</div>
  <div class="btn btn-small grid-c3 grid-r3">00:25</div>

  <span class="led led-off" aria-label="LED off"></span>
  <span class="led led-green" aria-label="Green LED"></span>
  <span class="led led-orange" aria-label="Orange LED"></span>
  <span class="led led-red" aria-label="Red LED"></span>

  <div class="btn btn-empty normal" aria-label="Empty button"></div>
</section>

<section class="state-set state-pressed" aria-label="Pressed state">
  <div class="btn btn-arrow col-1 row-a-arrow"><svg><use href="#icon-play"/></svg></div>
  <div class="btn btn-text col-2 row-a-text">Book<br>Now</div>
  <div class="btn btn-arrow col-1 row-b-arrow"><svg><use href="#icon-back"/></svg></div>
  <div class="btn btn-text col-2 row-b-text">Jetzt<br>Buchen</div>

  <div class="btn btn-small grid-c1 grid-r1"><svg><use href="#icon-first"/></svg></div>
  <div class="btn btn-small grid-c2 grid-r1"><svg><use href="#icon-last"/></svg></div>
  <div class="btn btn-small grid-c3 grid-r1"><svg><use href="#icon-arrow-left"/></svg></div>
  <div class="btn btn-small grid-c1 grid-r2">00:05</div>
  <div class="btn btn-small grid-c2 grid-r2">00:10</div>
  <div class="btn btn-small grid-c3 grid-r2"><svg><use href="#icon-return"/></svg></div>
  <div class="btn btn-small grid-c1 grid-r3">00:15</div>
  <div class="btn btn-small grid-c2 grid-r3">00:20</div>
  <div class="btn btn-small grid-c3 grid-r3">00:25</div>
</section>

<section class="state-set state-disabled" aria-label="Disabled state">
  <div class="btn btn-arrow col-1 row-a-arrow"><svg><use href="#icon-play"/></svg></div>
  <div class="btn btn-text col-2 row-a-text">Book<br>Now</div>
  <div class="btn btn-arrow col-1 row-b-arrow"><svg><use href="#icon-back"/></svg></div>
  <div class="btn btn-text col-2 row-b-text">Jetzt<br>Buchen</div>

  <div class="btn btn-small grid-c1 grid-r1"><svg><use href="#icon-first"/></svg></div>
  <div class="btn btn-small grid-c2 grid-r1"><svg><use href="#icon-last"/></svg></div>
  <div class="btn btn-small grid-c3 grid-r1"><svg><use href="#icon-arrow-left"/></svg></div>
  <div class="btn btn-small grid-c1 grid-r2">00:05</div>
  <div class="btn btn-small grid-c2 grid-r2">00:10</div>
  <div class="btn btn-small grid-c3 grid-r2"><svg><use href="#icon-return"/></svg></div>
  <div class="btn btn-small grid-c1 grid-r3">00:15</div>
  <div class="btn btn-small grid-c2 grid-r3">00:20</div>
  <div class="btn btn-small grid-c3 grid-r3">00:25</div>
</section>

</body>
</html>
```